Up to the Challenge? Canadian based consulting company needs a two sided business card design

A Canadian based security risk management consulting company needs a two-sided business card design. What we do is provide advice and guidance related to emergency, security and business continuity management for small, medium and large companies to help ensure the protection of their people, assets, information, services, operations and reputation.

The final design should be simple, only one or two colours, eye catching, professional and one that makes people look at three or more times just because it looks so darn good.

I have include examples of business cards I like.

Target Market(s)

Small, medium and large companies.

Industry/Entity Type

Security

Contact Information for Business Card

Business Card Size: Standard size of 3.5" (89mm) x 2.0" (51mm) - (see full specifications and guides on PRINTLY's website if required)
Card Stock: Looking to use PRINTLY's Velm 32pt stock textured paper - seam colour either chili red or black
Business Name: The Harrowgate Partners
Website: www.theharrowgatepartners.example
Telephone: (555)310-2968
Name: Dana Ostrander
Position: Principle
e-mail: Dana.Ostrander@theharrowgatepartners.example

Font styles to use
Serif

Colors
ec1f27
000000
9d9d9d
aaaaaa
606060

Requirements
Must have
• - "The Harrowgate Partners" logo (see uploaded files). I have included grey scale and colour versions.
• - Business card details (as above)
Nice to have
• - One side black or grey scale.
• - Other side would likely be white.
• - Everyone likes the silver logo on the black background.
• - Small element of colour i.e. red but I'm leaning more to greyscale.
Should not have
• - A lot of colour. Keep it simple.

```html
<!DOCTYPE html>
<html lang="en">
<head>
<meta charset="utf-8">
<title>The Harrowgate Partners – Business Card</title>
<link href="https://fonts.googleapis.com/css2?family=Cinzel:wght@400;600&display=swap" rel="stylesheet">
<style>
  :root {
    --backdrop: #e4e1dc;
    --stock: #eeece8;
    --ink: #3b3b3b;
    --ink-soft: #606060;
    --seam: #ec1f27;
    --shadow: rgba(0,0,0,0.18);
  }
  html, body {
    margin: 0;
    padding: 0;
    width: 1200px;
    height: 918px;
    overflow: hidden;
    background: var(--backdrop);
  }
  .canvas {
    position: relative;
    width: 1200px;
    height: 918px;
    font-family: "Cinzel", Georgia, serif;
    color: var(--ink);
  }
  .card {
    position: absolute;
    left: 265px;
    width: 670px;
    height: 383px;
    background: var(--stock);
    border-bottom: 6px solid var(--seam);
    box-shadow: 0 10px 24px var(--shadow);
    box-sizing: border-box;
  }
  .card--front { top: 48px; }
  .card--back { top: 481px; }

  /* Front */
  .brand {
    position: absolute;
    inset: 0;
    display: flex;
    align-items: center;
    justify-content: center;
    gap: 18px;
  }
  .brand__mark {
    width: 26px;
    height: 26px;
    background: var(--ink);
  }
  .brand__name {
    font-size: 34px;
    font-weight: 600;
    letter-spacing: 2px;
    text-transform: uppercase;
    color: var(--ink);
  }

  /* Back */
  .contact {
    position: absolute;
    left: 82px;
    top: 46px;
    width: 510px;
  }
  .contact__company {
    font-size: 40px;
    font-weight: 600;
    line-height: 1;
    letter-spacing: 1px;
    text-transform: uppercase;
    text-align: center;
  }
  .contact__company-sub {
    display: block;
    font-size: 26px;
    letter-spacing: 6px;
    margin-top: 6px;
    padding-left: 120px;
  }
  .contact__person {
    margin-top: 40px;
    font-size: 26px;
    letter-spacing: 1px;
    text-transform: uppercase;
  }
  .contact__rule {
    border: 0;
    border-top: 3px dotted var(--ink);
    margin: 6px 0;
  }
  .contact__line {
    font-size: 15px;
    letter-spacing: 0.5px;
    text-transform: uppercase;
    color: var(--ink-soft);
  }
  .contact__line--center { text-align: center; margin-top: 4px; }
</style>
</head>
<body>
<main class="canvas">
  <section class="card card--front" aria-label="Card front">
    <div class="brand">
      <span class="brand__mark"></span>
      <span class="brand__name">The Harrowgate Partners</span>
    </div>
  </section>

  <section class="card card--back" aria-label="Card back">
    <div class="contact">
      <h1 class="contact__company" style="margin:0">
        The Harrowgate
        <span class="contact__company-sub">Partners</span>
      </h1>
      <p class="contact__person" style="margin-bottom:0">Dana Ostrander – Principle</p>
      <hr class="contact__rule">
      <div class="contact__line">Dana.Ostrander@theharrowgatepartners.example</div>
      <hr class="contact__rule">
      <div class="contact__line">www.theharrowgatepartners.example</div>
      <div class="contact__line contact__line--center">(555)310-2968</div>
    </div>
  </section>
</main>
</body>
</html>
```